Varneck Bidding Business Cards Design Needed

I need a business card design that is modern looking - double sided (maybe just my logo on the back, but open to suggestions) - the overall design is up to you. I want it to be easy to read - not over the top flashy. I already have a company logo which I uploaded so that needs to be used. The colors of my logo are the colors I want on the card... so blue and gray (do need to match the logo colors).

Requirements
Must have
• Would like the card to be sleek, modern and easy to ready

```html
<!DOCTYPE html>
<html lang="en">
<head>
<meta charset="utf-8">
<title>Varneck Bidding – Business Cards</title>
<link href="https://fonts.googleapis.com/css2?family=Orbitron:wght@700&family=Roboto:wght@400;500&display=swap" rel="stylesheet">
<style>
  :root {
    --brand-blue: #3579b8;
    --brand-blue-deep: #2a6fb0;
    --brand-gray: #5c5f66;
    --paper: #f3f3f3;
    --stage: #e4e5e6;
    --white: #ffffff;
  }
  * { box-sizing: border-box; margin: 0; padding: 0; }
  html, body { width: 1200px; height: 726px; overflow: hidden; }
  body {
    background: var(--stage);
    font-family: "Roboto", Arial, sans-serif;
    position: relative;
  }
  .card {
    position: absolute;
    top: 214px;
    width: 520px;
    height: 297px;
    overflow: hidden;
    box-shadow: 0 6px 18px rgba(0,0,0,0.18);
  }
  .card--front { left: 50px; background: var(--brand-blue); color: var(--white); }
  .card--back { left: 630px; background: var(--paper); }

  .brand-name {
    font-family: "Orbitron", "Arial Black", sans-serif;
    font-weight: 700;
    letter-spacing: 0.5px;
    text-transform: uppercase;
    white-space: nowrap;
  }
  .tagline {
    font-family: "Roboto", Arial, sans-serif;
    font-weight: 500;
    text-transform: uppercase;
    letter-spacing: 0.5px;
    border-top: 1px solid currentColor;
    display: inline-block;
    white-space: nowrap;
  }

  /* front */
  .front-brand {
    position: absolute; left: 0; right: 0; top: 92px;
    text-align: center;
  }
  .front-brand .brand-name { font-size: 28px; line-height: 1.1; }
  .front-brand .tagline { font-size: 10px; padding-top: 4px; margin-top: 6px; }
  .front-url {
    position: absolute; left: 0; right: 0; top: 212px;
    display: flex; align-items: center; justify-content: center; gap: 18px;
    font-size: 13px; letter-spacing: 0.4px;
  }
  .front-url .rule { width: 62px; height: 2px; background: var(--white); }

  /* back */
  .back-shape { position: absolute; inset: 0; }
  .back-mark {
    position: absolute; left: 20px; top: 102px; width: 240px;
    text-align: center; color: var(--brand-blue);
  }
  .back-mark .brand-name { font-size: 28px; line-height: 1.3; }
  .back-info {
    position: absolute; right: 20px; top: 26px;
    text-align: right; color: var(--white);
  }
  .back-info .brand-name { font-size: 16px; line-height: 1.1; }
  .back-info .tagline { font-size: 6px; padding-top: 2px; margin-top: 3px; }
  .person-name {
    font-family: "Orbitron", "Arial Black", sans-serif;
    font-weight: 700;
    font-size: 14px; margin-top: 26px;
  }
  .person-role { font-size: 10px; margin-top: 3px; }
  .company { font-size: 12px; font-weight: 500; margin-top: 22px; }
  .contact-list { list-style: none; margin-top: 6px; }
  .contact-list li {
    font-size: 10.5px; line-height: 1.55;
    display: flex; align-items: center; justify-content: flex-end; gap: 6px;
  }
  .contact-list svg { width: 9px; height: 9px; fill: var(--white); }
</style>
</head>
<body>

<section class="card card--front" aria-label="Card front">
  <div class="front-brand">
    <div class="brand-name">Varneck Bidding</div>
    <div class="tagline">Brighter benefit auctions coast to coast</div>
  </div>
  <div class="front-url">
    <span class="rule"></span>
    <span>www.bidrevival.com</span>
    <span class="rule"></span>
  </div>
</section>

<section class="card card--back" aria-label="Card back">
  <svg class="back-shape" viewBox="0 0 520 297" width="520" height="297" aria-hidden="true">
    <path d="M222 0 Q330 95 318 297 L520 297 L520 0 Z" fill="var(--brand-gray)"/>
    <path d="M238 0 Q342 95 330 297 L520 297 L520 0 Z" fill="var(--brand-blue-deep)"/>
  </svg>

  <div class="back-mark">
    <div class="brand-name">Varneck<br>Bidding</div>
  </div>

  <div class="back-info">
    <div class="brand-name">Varneck Bidding</div>
    <div class="tagline">Brighter benefit auctions coast to coast</div>
    <div class="person-name">Morgan Tally</div>
    <div class="person-role">Owner/President - Auctioneer</div>
    <div class="company">Varneck Bidding, Inc.</div>
    <ul class="contact-list">
      <li>555-014-7730
        <svg viewBox="0 0 10 10"><path d="M1 3 Q5 0 9 3 L8 4.5 L6.5 3.8 L6.5 3 Q5 2.6 3.5 3 L3.5 3.8 L2 4.5 Z M2.5 5 L7.5 5 L8.5 9 L1.5 9 Z"/></svg>
      </li>
      <li>varneckbidding@mailbox.com
        <svg viewBox="0 0 10 10"><path d="M0.5 2 H9.5 V8 H0.5 Z M1.2 2.6 L5 5.6 L8.8 2.6 V7.4 H1.2 Z" fill-rule="evenodd"/></svg>
      </li>
      <li>www.bidrevival.com
        <svg viewBox="0 0 10 10"><circle cx="5" cy="5" r="4.5"/><path d="M0.8 5 H9.2 M5 0.6 V9.4 M5 0.6 Q2.4 5 5 9.4 M5 0.6 Q7.6 5 5 9.4" stroke="var(--brand-blue-deep)" stroke-width="0.7" fill="none"/></svg>
      </li>
    </ul>
  </div>
</section>

</body>
</html>
```